Etiketten für Imkerei mit Spezialisierung auf Bio Lagenhonig
Zielgruppe
wiesentau.at - BioImkerei Lindorf
Kleine Nebenerwerbs Imkerei mit Spezialisierung auf Bio Lagenhonig (nähere Infos sind auf der Website nachzulesen)
Als weitere Produktlinie bieten wir Wiesenfrucht / Honig mit Zutaten wie Himbeer, Erdbeer, Haselnuss, Mohn, Ingwer, Thymian, usw an.
Zielgruppe: Personen die offen für die Vielfalt der Natur sind, gesunde und natürliche Lebensmittel lieben und die bereit sind die aufwändige, großteils manuelle, Arbeit entsprechend zu entlohnen.
Gesucht:
ÄNDERUNG: Da die Anforderung für das ausgesetzte Preisgeld offensichtlich zu komplex ist, reduziere ich die Anforderung auf Etiketten für die Produktserie Wiesenfrucht, Gesamtkonzepte sind nicht erforderlich werden aber gerne angenommen.
ÜRSPRÜNGLICH:
Redesign der aktuellen Honigetiketten
Basisdesign für Lagenhonig und Wiesenfrucht das entsprechende Varianten zulässt.
Aufgabenstellung
Ich wünsche mir ein modernes, edles (oder Öko look) Design mit sehr guten Wiedererkennungswert das sich von gängigen Honigetiketten deutlich abhebt.
Das wiesentau Logo soll enthalten sein kann aber bei Bedarf angepasst werden (z.B. monocrome Verison)
Für Lagenhonig werden derzeit 400g und 100g Gläser mit hohem schwarzen DrehFix Decke und,
für Wiesenfrucht 250g und 100g mit hohem silbenen DrehFix Deckel verwendet. Beispiele sind im Webshop unter https://hofkorb.at/index.php/wiesentau ersichtilich.
Für das Ablaufdatum ist evtl. ein Feld für manuelle Stempelung vorzusehen.
Bitte die Sichtfeldregelung der EU Verpackungsverordnung einhalten.
Bisherige Etiketten hatten den Anspruch das diese auf guten Laserdruckern ausdruckbar waren - das ist jetzt nicht mehr zwingend notwendig (wäre für Kleinauflagen aber trotzdem vorteilhaft)

```html
<!DOCTYPE html>
<html lang="de">
<head>
<meta charset="utf-8">
<title>Wiesenfrucht Johannesbeere – Etikett</title>
<link rel="stylesheet" href="https://fonts.googleapis.com/css2?family=Allura&family=Fira+Sans:wght@400;600&display=swap">
<style>
  :root {
    --page: #ffffff;
    --honey: #f8b61c;
    --honey-light: #fbd686;
    --honey-deep: #ec8f12;
    --print: #ffffff;
  }
  * { margin: 0; padding: 0; box-sizing: border-box; }
  html, body {
    width: 1180px;
    height: 1200px;
    overflow: hidden;
    background: var(--page);
  }
  .canvas {
    position: relative;
    width: 1180px;
    height: 1200px;
  }
  .label {
    position: absolute;
    left: 122px;
    top: 230px;
    width: 936px;
    height: 740px;
    border-radius: 18px;
    background:
      linear-gradient(90deg, var(--honey-light) 0%, var(--honey) 22%, var(--honey) 60%, var(--honey-light) 100%);
    color: var(--print);
    font-family: "Fira Sans", sans-serif;
    overflow: hidden;
  }
  .label::before {
    content: "";
    position: absolute;
    left: 0; right: 0; bottom: 0;
    height: 60px;
    background: linear-gradient(180deg, rgba(236,143,18,0) 0%, var(--honey-deep) 100%);
    opacity: .5;
  }
  .line-name {
    position: absolute;
    left: 80px;
    top: 58px;
    font-size: 44px;
    font-weight: 600;
    letter-spacing: 0.5px;
    line-height: 1;
  }
  .rule {
    position: absolute;
    left: 0;
    height: 2px;
    background: var(--print);
  }
  .rule-top { top: 136px; width: 100%; }
  .rule-bottom { top: 665px; width: 530px; }
  .flavour {
    position: absolute;
    left: 0;
    width: 100%;
    top: 190px;
    text-align: center;
    font-family: "Allura", cursive;
    font-weight: 400;
    font-size: 160px;
    line-height: 1;
  }
  .tagline {
    position: absolute;
    left: 0;
    width: 100%;
    top: 384px;
    text-align: center;
    font-size: 44px;
    font-weight: 400;
    line-height: 1.1;
    letter-spacing: 0.3px;
  }
  .berry-motif {
    position: absolute;
    left: 360px;
    top: 478px;
    width: 180px;
    height: 108px;
    border-radius: 54px;
    background: radial-gradient(ellipse at center, rgba(255,255,255,.75) 0%, rgba(255,255,255,.15) 75%, rgba(255,255,255,0) 100%);
  }
  .website {
    position: absolute;
    left: 34px;
    top: 680px;
    font-size: 32px;
    line-height: 1.1;
  }
  .brand {
    position: absolute;
    right: 36px;
    top: 632px;
    font-size: 64px;
    font-weight: 600;
    letter-spacing: -0.5px;
    line-height: 1;
  }
</style>
</head>
<body>
  <main class="canvas">
    <section class="label">
      <p class="line-name">WIESENFRUCHT</p>
      <div class="rule rule-top"></div>
      <h1 class="flavour">Johannesbeere</h1>
      <p class="tagline">Sanft vereint mit Blütenhonig</p>
      <div class="berry-motif" role="img" aria-label="Zeichnung eines Johannisbeerzweigs"></div>
      <div class="rule rule-bottom"></div>
      <p class="website">www.wiesentau.at</p>
      <p class="brand">wiesentau</p>
    </section>
  </main>
</body>
</html>
```